Stationery Design needed for logo design project

This company needs a letterhead and envelope for their new practice. We did not want to release this contact until the business card design was finalized so the stationary can be created to coordinate with it.

For those of you that will be submitting designs for this content, think "linear". Designs with curves or "swooshes" are not appropriate for this design.

NOTE: As part of the source files; I will require FULLY LAYERED PHOTOSHOP FILES of all elements, including design elements, text and fonts. If you cannot provide a fully layered PSD file, please do not submit.
Updates

The project details have been updated. We have added a new description along with logo files and business card design. Please review the style of the logo and business card before submitting designs. Thanks

Target Market(s)

Medical

Industry/Entity Type

Business

Requirements
Must have
• NOTE: As part of the source files; I will require FULLY LAYERED PHOTOSHOP FILES of all elements, including design elements, text and fonts. If you cannot provide a fully layered PSD file, please do not submit.

Logo
2 office address locations
phone
fax
email
website URL

```html
<!DOCTYPE html>
<html lang="en">
<head>
<meta charset="utf-8">
<title>Marlow &amp; Associates – Stationery Set</title>
<link href="https://fonts.googleapis.com/css2?family=Barlow:wght@400;500;600&display=swap" rel="stylesheet">
<style>
  :root{
    --red:#c0213a;
    --red-deep:#6e0f1f;
    --ink:#2b2b2b;
    --paper:#ffffff;
    --frame:#c9c9c9;
    --edge:#bdbdbd;
  }
  *{box-sizing:border-box;margin:0;padding:0}
  html,body{width:1200px;height:850px;overflow:hidden;background:var(--paper)}
  body{font-family:"Barlow",Arial,sans-serif;color:var(--ink);position:relative}
  .board{position:absolute;inset:0;border:1px solid var(--frame)}
  .sheet{position:absolute;background:var(--paper);border:1px solid var(--edge);box-shadow:3px 5px 7px rgba(0,0,0,.28);overflow:hidden}
  .brand{position:absolute;display:flex;align-items:center;gap:6px;font-weight:600;color:var(--ink);letter-spacing:.04em;white-space:nowrap}
  .brand-dot{width:10px;height:10px;border-radius:50%;background:var(--red);flex:none}

  .row{display:flex;align-items:center;gap:3px;white-space:nowrap}
  .ico{width:7px;height:7px;flex:none}

  /* business card front */
  .card-front{left:28px;top:175px;width:242px;height:142px}
  .card-front .brand{left:62px;top:62px;font-size:13px}

  /* business card back */
  .card-back{left:303px;top:175px;width:242px;height:142px;border:none;
    background:linear-gradient(90deg,var(--red) 0%,var(--red-deep) 100%);
    color:#fff;font-size:7.5px;line-height:9px}
  .card-back .ico{fill:#fff}
  .card-back .holder{position:absolute;left:19px;top:9px}
  .card-back .holder b{font-weight:600;display:block}
  .card-back .rule{position:absolute;height:1px;background:rgba(255,255,255,.75);left:19px}
  .card-back .contacts{position:absolute;left:19px;top:48px}
  .card-back .office{position:absolute;left:15px;top:104px}
  .card-back .office b{font-weight:600;display:block}

  /* footer contact block (envelope + letterhead) */
  .footer-block{position:absolute;font-size:7.5px;line-height:10px}
  .footer-block .name{color:var(--red);font-weight:600;letter-spacing:.03em}
  .footer-block .line{position:relative;height:1px;background:var(--red);margin:4px 0 5px}
  .footer-block .line::after{content:"";position:absolute;right:-3px;top:-2px;width:5px;height:5px;border:1px solid var(--red);border-radius:50%;background:var(--paper)}
  .footer-block .items{display:flex;gap:8px}
  .footer-block .ico{fill:var(--red)}

  /* letterhead */
  .letterhead{left:610px;top:30px;width:551px;height:780px;z-index:1}
  .letterhead .brand{right:22px;top:30px;font-size:14px}
  .letterhead .footer-block{right:26px;top:717px;width:318px;text-align:right}
  .letterhead .footer-block .line::after{right:auto;left:-3px}
  .letterhead .footer-block .items{justify-content:flex-end}

  /* envelope (sits over the letterhead) */
  .envelope{left:28px;top:411px;width:694px;height:300px;z-index:2;border-right:none;overflow:visible;border-radius:0 10px 10px 0}
  .envelope .flap{position:absolute;right:-1px;top:-1px;width:28px;height:calc(100% + 2px);
    background:linear-gradient(180deg,#b8263f 0%,var(--red-deep) 100%);border-radius:0 10px 10px 0}
  .envelope .brand{left:22px;top:26px;font-size:14px}
  .envelope .footer-block{left:22px;top:242px;width:316px}

  .label{position:absolute;left:27px;top:813px;font-size:15px;color:var(--ink)}
</style>
</head>
<body>
<svg width="0" height="0" style="position:absolute" aria-hidden="true">
  <symbol id="i-phone" viewBox="0 0 10 10"><path d="M1 3.5C1 2 2.5 1.5 5 1.5S9 2 9 3.5L7.5 4.5 6.8 3.6H3.2L2.5 4.5ZM2.5 5H7.5L8.5 8.5H1.5Z"/></symbol>
  <symbol id="i-fax" viewBox="0 0 10 10"><path d="M2.5 0.8H7.5V3.5H2.5ZM0.8 3.8H9.2V8H7.5V6.5H2.5V8H0.8ZM3 7H7V9.2H3Z"/></symbol>
  <symbol id="i-mobile" viewBox="0 0 10 10"><path d="M3 0.5H7V9.5H3ZM3.8 1.5V7.5H6.2V1.5Z"/></symbol>
  <symbol id="i-mail" viewBox="0 0 10 10"><path d="M0.5 2H9.5V8H0.5ZM1.2 2.6 5 5.4 8.8 2.6Z"/></symbol>
  <symbol id="i-web" viewBox="0 0 10 10"><path d="M5 0.5A4.5 4.5 0 1 0 5 9.5 4.5 4.5 0 1 0 5 0.5ZM5 2A3 3 0 1 1 5 8 3 3 0 1 1 5 2Z"/></symbol>
</svg>

<main class="board">

  <section class="sheet card-front" aria-label="Business card front">
    <div class="brand"><span class="brand-dot"></span>MARLOW &amp; ASSOCIATES</div>
  </section>

  <section class="sheet card-back" aria-label="Business card back">
    <div class="holder">
      <b>Your Name</b>
      <div class="row"><svg class="ico"><use href="#i-mobile"/></svg>(555) 010-4567</div>
    </div>
    <div class="rule" style="top:37px;width:89px"></div>
    <div class="contacts">
      <div class="row"><svg class="ico"><use href="#i-phone"/></svg>(555) 010-4567</div>
      <div class="row"><svg class="ico"><use href="#i-fax"/></svg>(555) 010-4567</div>
      <div class="row"><svg class="ico"><use href="#i-mail"/></svg>info@marlowcardiology.com</div>
      <div class="row"><svg class="ico"><use href="#i-web"/></svg>www.marlowcardiology.com</div>
    </div>
    <div class="rule" style="top:94px;width:122px"></div>
    <div class="office">
      <b>MARLOW &amp; ASSOCIATES</b>
      This is dummy address text<br>original text will be replace here...
    </div>
  </section>

  <section class="sheet letterhead" aria-label="Letterhead">
    <div class="brand"><span class="brand-dot"></span>MARLOW &amp; ASSOCIATES</div>
    <div class="footer-block">
      <div class="name">MARLOW &amp; ASSOCIATES</div>
      <div class="line"></div>
      <div>This is dummy address text original text will be replace here</div>
      <div class="items">
        <span class="row"><svg class="ico"><use href="#i-phone"/></svg>(555) 010-4567</span>
        <span class="row"><svg class="ico"><use href="#i-fax"/></svg>(555) 010-4567</span>
        <span class="row"><svg class="ico"><use href="#i-mail"/></svg>info@marlowcardiology.com</span>
        <span class="row"><svg class="ico"><use href="#i-web"/></svg>www.marlowcardiology.com</span>
      </div>
    </div>
  </section>

  <section class="sheet envelope" aria-label="Envelope">
    <div class="flap"></div>
    <div class="brand"><span class="brand-dot"></span>MARLOW &amp; ASSOCIATES</div>
    <div class="footer-block">
      <div class="name">MARLOW &amp; ASSOCIATES</div>
      <div class="line"></div>
      <div>This is dummy address text original text will be replace here...</div>
      <div class="items">
        <span class="row"><svg class="ico"><use href="#i-phone"/></svg>(555) 010-4567</span>
        <span class="row"><svg class="ico"><use href="#i-fax"/></svg>(555) 010-4567</span>
        <span class="row"><svg class="ico"><use href="#i-mail"/></svg>info@marlowcardiology.com</span>
        <span class="row"><svg class="ico"><use href="#i-web"/></svg>www.marlowcardiology.com</span>
      </div>
    </div>
  </section>

  <p class="label">Options 02</p>
</main>
</body>
</html>
```